jot school poster design and change logo name

We already have a logo which only needs to be slightly modified with "school".
We also have two advertising faces, a girl and a boy, which should be on our poster.
Important key data:

bilingual D/E small classes
daycare
private kindergarten
private school from 2024

Poster size: 268,5 x 128 cm
We need logo sizes in different sizes
also for T-shirts.
Attached also a old poster

new clients

0094D4
00A9DD
6FCCEA
C7EBF8
E9F6FB
59FF00
82FF00
B8FF75
E3FFCB
F4FFEA
FFC000
F8CF3A
FAE287
FDF2CF
FEFAEE
F0912C
F2A743
F7CA91
FBE8D2
FDF5EE

```html
<!DOCTYPE html>
<html lang="de">
<head>
<meta charset="utf-8">
<title>jot school – Kinderkrippe &amp; Hort</title>
<link rel="stylesheet" href="https://fonts.googleapis.com/css2?family=Schoolbell&family=Sniglet:wght@400;800&display=swap">
<style>
  :root {
    --blue-deep: #0094D4;
    --blue: #00A9DD;
    --teal: #3FB5B5;
    --teal-light: #7FD3CE;
    --green: #8CC63F;
    --green-lime: #9BD22A;
    --orange: #F7A21B;
    --orange-deep: #F0912C;
    --yellow: #FFC000;
    --pink: #EE4A9B;
    --cream: #FDE9A8;
    --white: #FFFFFF;
    --page: #E6E7E9;
  }
  * { box-sizing: border-box; margin: 0; padding: 0; }
  html, body { width: 1200px; height: 900px; overflow: hidden; background: var(--page); }
  .flyer {
    position: absolute; left: 50px; top: 190px;
    width: 1100px; height: 520px;
    background: var(--white);
    overflow: hidden;
    font-family: "Sniglet", system-ui, sans-serif;
    box-shadow: 0 6px 20px rgba(0,0,0,.18);
  }
  .flyer__backdrop, .flyer__waves { position: absolute; inset: 0; }
  .flyer__photo {
    position: absolute; left: 60px; top: 150px; width: 360px; height: 320px;
    background: radial-gradient(ellipse at 50% 45%, #F3D2BC 0%, #D7AC8A 45%, #9A6B4A 85%, #8A5E3F 100%);
    border-radius: 46% 46% 8% 8%;
  }
  .headline {
    position: absolute; left: 300px; top: 32px; width: 440px;
    color: var(--white); font-size: 24px; line-height: 1.25; text-align: center;
  }
  .bubble__text {
    position: absolute; left: 440px; top: 198px; width: 175px;
    font-family: "Schoolbell", "Comic Sans MS", cursive; color: var(--white);
    font-size: 25px; line-height: 1.1; text-align: center;
  }
  .brand {
    position: absolute; left: 810px; top: 64px; width: 290px;
    display: flex; justify-content: center; align-items: center; gap: 10px;
    color: var(--orange-deep); font-weight: 800; font-size: 40px; white-space: nowrap;
  }
  .brand__dot { width: 22px; height: 22px; border-radius: 50%; background: var(--orange-deep); }
  .offer { position: absolute; left: 560px; top: 262px; width: 520px; text-align: center; }
  .offer__title {
    font-family: "Schoolbell", "Comic Sans MS", cursive;
    color: var(--green-lime); font-size: 60px; font-weight: 400; line-height: 1; white-space: nowrap;
  }
  .offer__age { color: var(--blue-deep); font-size: 26px; line-height: 1.15; margin-top: 10px; }
  .contact {
    position: absolute; left: 40px; right: 40px; bottom: 18px;
    display: flex; justify-content: space-between; align-items: center;
    color: var(--white); font-size: 20px;
  }
  .contact__item { display: flex; align-items: center; gap: 8px; }
  .contact__icon { width: 22px; height: 22px; }
</style>
</head>
<body>
  <main class="flyer">
    <svg class="flyer__backdrop" viewBox="0 0 1100 520" aria-hidden="true">
      <defs>
        <linearGradient id="sunband" x1="0" y1="0" x2="0" y2="1">
          <stop offset="0" stop-color="#F7A21B"/>
          <stop offset="1" stop-color="#FBC21A"/>
        </linearGradient>
      </defs>
      <path d="M0 0 H1100 V170 C900 260 700 270 550 250 C350 225 150 250 0 330 Z" fill="url(#sunband)"/>
      <path d="M0 330 C150 250 350 225 550 250 C700 270 900 260 1100 170 L1100 180 C900 272 700 282 550 262 C350 238 150 262 0 344 Z" fill="var(--green)"/>
      <ellipse cx="965" cy="92" rx="185" ry="120" fill="var(--cream)"/>
      <ellipse cx="975" cy="86" rx="175" ry="112" fill="var(--white)"/>
    </svg>

    <div class="flyer__photo" role="img" aria-label="Foto: lachendes Mädchen mit bunt bemalten Händen"></div>

    <svg class="flyer__waves" viewBox="0 0 1100 520" aria-hidden="true">
      <path d="M440 195 C450 175 500 178 540 182 C580 172 615 182 615 215 C620 250 598 275 560 275 L510 277 L478 322 L485 277 C455 275 430 255 435 232 Z" fill="var(--pink)"/>
      <path d="M450 203 C460 188 500 190 540 193 C578 186 604 194 604 216 C608 244 590 264 558 264 L488 266 C460 264 444 250 446 232 Z" fill="none" stroke="var(--white)" stroke-width="2"/>
      <path d="M0 460 C250 430 450 450 650 430 C850 410 950 400 1100 380 V520 H0 Z" fill="var(--teal-light)"/>
      <path d="M0 476 C250 450 450 468 650 448 C850 428 950 420 1100 402 V520 H0 Z" fill="var(--teal)"/>
    </svg>

    <p class="headline">Bei uns lernen ALLE Kinder spielnd einfach in kürzester Zeit Englisch wie einee 2. Muttersprache</p>

    <p class="bubble__text">Do you speak English?</p>

    <div class="brand"><span class="brand__dot"></span><span class="brand__name">jot school</span></div>

    <section class="offer">
      <h1 class="offer__title">Kinderkrippe &amp; Hort</h1>
      <p class="offer__age">Ab 3. Lebensmonat bis zum<br>12. Lebensjahr</p>
    </section>

    <footer class="contact">
      <span class="contact__item">
        <svg class="contact__icon" viewBox="0 0 24 24" aria-hidden="true"><circle cx="12" cy="12" r="11" fill="var(--yellow)"/><path d="M12 5a4 4 0 0 0-4 4c0 3 4 9 4 9s4-6 4-9a4 4 0 0 0-4-4z" fill="var(--white)"/><circle cx="12" cy="9" r="1.5" fill="var(--yellow)"/></svg>
        Lindenweg 12, 8000 Musterdorf
      </span>
      <span class="contact__item">
        <svg class="contact__icon" viewBox="0 0 24 24" aria-hidden="true"><circle cx="12" cy="12" r="11" fill="var(--yellow)"/><circle cx="12" cy="12" r="6" fill="none" stroke="var(--white)" stroke-width="1.5"/><path d="M6 12h12M12 6c-2.5 3-2.5 9 0 12M12 6c2.5 3 2.5 9 0 12" fill="none" stroke="var(--white)" stroke-width="1.5"/></svg>
        www.jot-daycare.ch
      </span>
      <span class="contact__item">
        <svg class="contact__icon" viewBox="0 0 24 24" aria-hidden="true"><circle cx="12" cy="12" r="11" fill="var(--yellow)"/><path d="M8 6l2.5 0 1 3-1.5 1.2a8 8 0 0 0 3.8 3.8L15 12.5l3 1V16c0 1-1 1.5-2 1.5A9.5 9.5 0 0 1 6.5 8C6.5 7 7 6 8 6z" fill="var(--white)"/></svg>
        +41 79 000 12 34
      </span>
    </footer>
  </main>
</body>
</html>
```